Solvane Vitality MediSpa Brochure

We need a new brochure design. The old is attached.

We are wanting a three panel brochure for med spa designed and ready for print. The brochure will have content and images on both sides. We attached the old brochure in pdf format. The content needs to stay as on the attached pdf but please feel free to offer new designs. The color needs to match the attached logo, which is a light blue and teal. All images we want on the brochure are also attached.

The design must have an 1/8 in space from each edge for printing purposes

Target Market(s)

Men and Women

Industry/Entity Type

Wellness

Font styles to use
Sans Serif

Colors
34a6d7
33b8a4

Requirements
Must have
• soft curves. must have a 1/8 in space on all edges (including interior) to give bleed space for printing. Use content written on attached brochure.

```html
<!DOCTYPE html>
<html lang="en">
<head>
<meta charset="utf-8">
<title>Solvane Vitality MediSpa – Trifold Brochure</title>
<link href="https://fonts.googleapis.com/css2?family=Zilla+Slab:wght@300;400;600;700&family=Merriweather:wght@300;400&family=Fira+Sans+Condensed:wght@300;400;500&family=Open+Sans:wght@400;600&display=swap" rel="stylesheet">
<style>
:root{
  --teal:#1a9ea0;
  --teal-dark:#107f83;
  --teal-deep:#0d6f73;
  --teal-soft:#7fcfd0;
  --sky:#d5eef1;
  --ink:#6a6a6a;
  --paper:#ffffff;
  --stage:#d6d7d9;
  --mist:#eceeef;
}
*{box-sizing:border-box;margin:0;padding:0}
html,body{width:1200px;height:960px;overflow:hidden}
body{background:var(--stage);position:relative;font-family:"Merriweather",serif}
.brochure{position:absolute;left:30px;top:40px;width:1140px;height:880px;display:flex;box-shadow:0 6px 24px rgba(0,0,0,.18)}
.panel{position:relative;width:380px;height:880px;background:var(--paper);overflow:hidden}
.panel + .panel{border-left:1px solid #e3e5e6}
.panel-bg{position:absolute;inset:0;width:380px;height:880px}
.abs{position:absolute}
.rule{border-top:1px dotted #9aa;}

/* panel 1 */
.intro{left:24px;top:40px;width:320px}
.intro-kicker{font-family:"Zilla Slab",serif;font-weight:300;font-size:30px;color:var(--teal);line-height:1}
.intro-title{font-family:"Zilla Slab",serif;font-weight:700;font-size:30px;color:var(--teal);line-height:1.1}
.intro .rule{margin:6px 0 10px}
.intro-body{font-size:13px;line-height:1.38;color:var(--teal);font-weight:300}
.why{right:24px;top:262px;width:320px;text-align:right}
.why-kicker{font-family:"Zilla Slab",serif;font-weight:300;font-size:27px;color:var(--ink);line-height:1.05}
.why-title{font-family:"Zilla Slab",serif;font-weight:700;font-size:27px;color:var(--ink);line-height:1.1}
.why .rule{margin:8px 0 10px}
.why-body{font-size:12.5px;line-height:1.4;color:#8a8a8a;font-weight:300;margin-bottom:10px}
.members{left:34px;top:588px;width:300px;color:#fff}
.members-kicker{font-family:"Zilla Slab",serif;font-weight:300;font-size:26px;line-height:1}
.members-title{font-family:"Zilla Slab",serif;font-weight:700;font-size:26px;line-height:1.15}
.members .rule{border-color:rgba(255,255,255,.6);margin:6px 0 8px}
.members-body{font-size:12.5px;line-height:1.35;font-weight:300}
.tiers{left:20px;top:750px;display:flex;gap:4px}
.tier{width:100px;height:58px;background:var(--teal);color:#fff;text-align:center;padding-top:9px}
.tier-name{font-family:"Zilla Slab",serif;font-weight:700;font-size:15px;letter-spacing:.5px}
.tier-sub{font-family:"Zilla Slab",serif;font-size:13px}
.learn{left:0;width:380px;top:826px;text-align:center;color:#fff}
.learn-kicker{font-family:"Zilla Slab",serif;font-size:14px}
.learn-url{font-family:"Zilla Slab",serif;font-weight:600;font-size:12.5px}

/* panel 2 */
.portrait{left:118px;top:24px;width:144px;height:144px;border-radius:50%;border:5px solid #fff;box-shadow:0 0 0 2px var(--teal-soft);background:radial-gradient(circle at 50% 40%,#c9a58c,#6b4a38 70%,#3f5a3a)}
.doctor{left:0;width:380px;top:182px;text-align:center}
.doctor-name{font-family:"Fira Sans Condensed",sans-serif;font-weight:500;font-size:21px;color:var(--teal)}
.doctor-cred{font-family:"Fira Sans Condensed",sans-serif;font-size:12px;color:#666}
.doctor .rule{width:220px;margin:8px auto 0}
.quotes{left:26px;top:246px;width:328px}
.quote{font-family:"Fira Sans Condensed",sans-serif;font-weight:300;font-size:13.5px;line-height:1.3;color:var(--teal);text-align:justify;margin-bottom:10px}
.consult{left:22px;top:490px;width:336px;height:140px;background:var(--sky);padding:12px 18px}
.consult-title{font-family:"Fira Sans Condensed",sans-serif;font-weight:500;font-size:18px;color:var(--teal);text-align:center}
.consult-line{font-family:"Fira Sans Condensed",sans-serif;font-weight:300;font-size:20px;color:#9fcfd6;text-align:center;line-height:1.3}
.consult-line small{font-size:13px}
.consult-mail{font-family:"Fira Sans Condensed",sans-serif;font-size:16px;color:var(--teal);text-align:center;margin-top:4px}
.brand{display:flex;align-items:center;justify-content:center;gap:10px;font-family:"Open Sans",sans-serif;font-weight:600;color:var(--teal);text-align:center}
.brand-dot{width:14px;height:14px;border-radius:50%;background:var(--teal);flex:none}
.brand-small{left:0;width:380px;top:656px;font-size:21px;line-height:1.15}
.address{left:0;width:380px;top:712px;text-align:center;font-family:"Merriweather",serif;font-size:13px;color:#555;line-height:1.45}
.visit{left:26px;top:826px;color:#fff}
.visit-kicker{font-family:"Zilla Slab",serif;font-size:13px}
.visit-url{font-family:"Zilla Slab",serif;font-weight:600;font-size:15px}

/* panel 3 */
.tagline{left:0;width:380px;top:18px;text-align:center;font-family:"Zilla Slab",serif;font-weight:700;color:var(--teal-soft);font-size:32px;line-height:1}
.tagline-amp{display:block;font-weight:300;font-size:26px;color:#bfe7e8}
.hero{left:0;top:150px;width:380px;height:420px;background:linear-gradient(135deg,#f3dccd 0%,#e7b7a0 45%,#c98f7a 75%,#f4e6de 100%)}
.brand-large{left:0;width:380px;top:600px;font-size:30px;line-height:1.15}
.offer{left:20px;top:720px;display:flex;gap:14px}
.audience{width:130px;text-align:right;font-family:"Zilla Slab",serif;font-style:italic;font-weight:400;font-size:26px;color:var(--teal);line-height:1.05;padding-top:36px}
.services{list-style:none;border-left:1px dotted #999;padding-left:14px}
.services li{font-family:"Merriweather",serif;font-size:13.5px;color:#444;line-height:1.8;display:flex;align-items:center;gap:10px}
.services li:nth-child(odd){color:var(--teal)}
.services li::before{content:"";width:0;height:0;border-left:10px solid transparent;border-bottom:10px solid currentColor}
</style>
</head>
<body>
<main class="brochure">

  <!-- inside-left panel -->
  <section class="panel panel-about">
    <svg class="panel-bg" viewBox="0 0 380 880" aria-hidden="true">
      <path d="M130 0 H380 V72 Q260 30 130 0Z" fill="var(--teal)"/>
      <path d="M220 0 H380 V40 Q300 12 220 0Z" fill="var(--teal-dark)"/>
      <path d="M0 500 Q190 520 340 560 L380 570 V880 H0Z" fill="var(--teal)"/>
      <path d="M0 540 L330 572 L336 810 L0 846Z" fill="var(--teal-dark)"/>
      <path d="M0 846 L336 810 L380 804 V880 H0Z" fill="var(--teal-deep)"/>
    </svg>
    <div class="abs intro">
      <h2 class="intro-kicker">Brookmere’s</h2>
      <h1 class="intro-title">Premier Medispa</h1>
      <div class="rule"></div>
      <p class="intro-body">Solvane Vitality Medispa is the premier medical spa in Brookmere, TX. We utilize the best equipment available today for laser treatments, dermal fillers, facials, injections, chemical peels and wellness solutions.</p>
    </div>
    <div class="abs why">
      <h2 class="why-kicker">Why choose our</h2>
      <h2 class="why-title">Medispa?</h2>
      <div class="rule"></div>
      <p class="why-body">Under the supervision of Dr. Elena Marsh, our medical staff provides state-of-the-art cosmetic treatment to both women and men.</p>
      <p class="why-body">Our staff is trained to provide unique medical spa services to help our clients achieve a more youthful look and defy the aging process.</p>
    </div>
    <div class="abs members">
      <h2 class="members-kicker">Exclusive</h2>
      <h2 class="members-title">Memberships</h2>
      <div class="rule"></div>
      <p class="members-body">Our exclusive membership packages are tailored for our clients and created to give them an exceptional experience at a discounted price.</p>
    </div>
    <div class="abs tiers">
      <div class="tier"><div class="tier-name">SILVER</div><div class="tier-sub">Membership</div></div>
      <div class="tier"><div class="tier-name">GOLD</div><div class="tier-sub">Membership</div></div>
      <div class="tier"><div class="tier-name">PLATINUM</div><div class="tier-sub">Membership</div></div>
    </div>
    <div class="abs learn">
      <div class="learn-kicker">Learn More At</div>
      <div class="learn-url">www.SolvaneVitalityMedispa.com/memberships</div>
    </div>
  </section>

  <!-- inside-middle panel -->
  <section class="panel panel-doctor">
    <svg class="panel-bg" viewBox="0 0 380 880" aria-hidden="true">
      <path d="M0 0 H380 V150 Q200 90 0 40Z" fill="var(--teal)"/>
      <path d="M0 40 Q200 90 380 150 V180 Q200 120 0 70Z" fill="var(--sky)"/>
      <path d="M0 780 Q200 790 380 840 V880 H0Z" fill="var(--teal)"/>
      <path d="M0 760 Q160 770 300 800 L0 800Z" fill="var(--sky)"/>
    </svg>
    <div class="abs portrait" role="img" aria-label="Portrait photograph of the supervising physician"></div>
    <div class="abs doctor">
      <div class="doctor-name">Dr. Elena Marsh</div>
      <div class="doctor-cred">MD FACS</div>
      <div class="rule"></div>
    </div>
    <div class="abs quotes">
      <p class="quote">“Rejuvenation and reconstruction of the face are my passion, whether it is to improve one’s visual functions or to enhance one’s appearance.”</p>
      <p class="quote">“I personally perform all of my injections and CO2 laser treatments because safety and satisfaction are my top priorities.”</p>
      <p class="quote">“I was called to become a physician at the age of seven years old. I am motivated by a desire to serve others by providing superb medical care. I constantly strive to do my best.”</p>
    </div>
    <div class="abs consult">
      <div class="consult-title">Schedule a Consultation</div>
      <div class="consult-line"><small>Ph:</small> (555) 014-2290</div>
      <div class="consult-line"><small>Fax:</small> (555) 014-2291</div>
      <div class="consult-mail">glow@elenamarshmd.com</div>
    </div>
    <div class="abs brand brand-small"><span class="brand-dot"></span><span>Solvane Vitality<br>MediSpa</span></div>
    <address class="abs address">48 Harrow Lane<br>Suite 12, Brookmere, TX 75000</address>
    <div class="abs visit">
      <div class="visit-kicker">For more details visit us on</div>
      <div class="visit-url">www.SolvaneVitalityMedispa.com</div>
    </div>
  </section>

  <!-- front cover panel -->
  <section class="panel panel-cover">
    <svg class="panel-bg" viewBox="0 0 380 880" aria-hidden="true">
      <defs>
        <linearGradient id="mist" x1="0" y1="0" x2="0" y2="1">
          <stop offset="0" stop-color="#ffffff"/>
          <stop offset="1" stop-color="var(--mist)"/>
        </linearGradient>
      </defs>
      <rect x="0" y="570" width="380" height="310" fill="url(#mist)"/>
      <path d="M0 0 H380 V170 H0Z" fill="var(--teal)"/>
      <path d="M0 690 Q200 740 380 700 V740 Q200 790 0 730Z" fill="#dfe2e3"/>
      <path d="M0 850 Q200 830 380 840 V880 H0Z" fill="var(--teal)"/>
    </svg>
    <h2 class="abs tagline">Refresh<span class="tagline-amp">&amp;</span>Rejuvenate</h2>
    <div class="abs hero" role="img" aria-label="Close-up beauty photograph of a client with smooth, radiant skin"></div>
    <div class="abs brand brand-large"><span class="brand-dot"></span><span>Solvane Vitality<br>MediSpa</span></div>
    <div class="abs offer">
      <div class="audience">For<br>Women<br>&amp; Men</div>
      <ul class="services">
        <li>Laser Treatments</li>
        <li>Dermal Fillers</li>
        <li>Neurotoxins</li>
        <li>Facials</li>
        <li>Chemical Peels</li>
        <li>Wellness Treatments</li>
      </ul>
    </div>
  </section>

</main>
</body>
</html>
```